TriVex Business Card Design - double sided -plumbing local plumbing company

We have a Plumbing company where the design was create through Sketch Hive. We would now like a business card designed as well. We want it to be in the colour version of the logo.

Details below for the card.

Phone Number: 0438 615 247
Email: info@trivexplumbing.example.au
Website: https://trivexplumbing.example.au
We really want a sophisticated design that stand out from the other- informative and timeless.

Target Market(s)

local Canberra market

Industry/Entity Type

Plumbing, gas fitting, hot water

Contact Information for Business Card

Phone number, email, logo and "Supplying all your heating, cooling and hot water needs"

Requirements
Must have
• bust be colourful, must also be though about it being printed on a magnet. must Vex with the logo - I dont want the logo and information chucked onto a white canvas I would prefer it to be smooth and look purposeful

```html
<!DOCTYPE html>
<html lang="en">
<head>
<meta charset="utf-8">
<title>TriVex Business Card</title>
<link rel="stylesheet" href="https://fonts.googleapis.com/css2?family=Open+Sans:wght@400;600;700;800&display=swap">
<style>
  :root {
    --bg: #d6d6d6;
    --paper: #f4f4f4;
    --blue: #1b8fd6;
    --orange: #e69a22;
    --ink: #1a1a1a;
    --white: #ffffff;
  }
  * { margin: 0; padding: 0; box-sizing: border-box; }
  html, body {
    width: 1200px; height: 1051px; overflow: hidden;
    background: var(--bg);
    font-family: "Open Sans", sans-serif;
  }
  .canvas {
    width: 1200px; height: 1051px;
    display: flex; flex-direction: column; align-items: center; justify-content: center;
    gap: 56px;
  }
  .card {
    position: relative;
    width: 640px; height: 391px;
    background: var(--paper);
    border-bottom: 6px solid var(--blue);
    box-shadow: 0 14px 30px rgba(0,0,0,0.22);
    overflow: hidden;
  }
  .wordmark {
    display: flex; align-items: center; gap: 18px;
    font-weight: 800; color: var(--blue);
    letter-spacing: 2px; line-height: 1;
  }
  .wordmark-dot {
    border-radius: 50%; background: var(--orange); flex: none;
  }

  /* Back side */
  .card-back .wordmark { position: absolute; left: 70px; top: 70px; font-size: 118px; }
  .card-back .wordmark-dot { width: 56px; height: 56px; }
  .tagline-band {
    position: absolute; left: 0; right: 0; top: 250px; height: 30px;
    background: var(--orange);
    display: flex; align-items: center; padding-left: 60px;
    color: var(--white); font-size: 15px; letter-spacing: 0.3px;
  }

  /* Front side */
  .card-front .wordmark { position: absolute; left: 50px; top: 48px; font-size: 104px; }
  .card-front .wordmark-dot { width: 48px; height: 48px; }
  .person {
    position: absolute; left: 50px; top: 262px; width: 200px; text-align: right;
  }
  .person-name { font-size: 20px; font-weight: 700; letter-spacing: 0.5px; }
  .person-name .first { color: var(--blue); }
  .person-name .last { color: var(--orange); }
  .person-role { font-size: 14px; color: var(--ink); margin-top: 2px; }
  .divider {
    position: absolute; left: 270px; top: 258px; width: 2px; height: 76px;
    background: var(--blue);
  }
  .contacts {
    position: absolute; left: 290px; top: 262px;
    list-style: none; font-size: 15px; color: var(--ink);
  }
  .contacts li { display: flex; align-items: center; gap: 8px; line-height: 23px; }
  .contacts svg { width: 13px; height: 13px; flex: none; }
</style>
</head>
<body>
<main class="canvas">

  <section class="card card-back" aria-label="Business card back">
    <div class="wordmark"><span>TriVex</span><span class="wordmark-dot"></span></div>
    <div class="tagline-band">Supplying all your heating, cooling and hot water needs</div>
  </section>

  <section class="card card-front" aria-label="Business card front">
    <div class="wordmark"><span>TriVex</span><span class="wordmark-dot"></span></div>

    <div class="person">
      <p class="person-name"><span class="first">LIAM</span> <span class="last">CARTER</span></p>
      <p class="person-role">Managing Director</p>
    </div>
    <div class="divider"></div>

    <ul class="contacts">
      <li>
        <svg viewBox="0 0 16 16" aria-hidden="true"><path fill="var(--blue)" d="M3.6 1.2l2.3 2.9-1.3 1.6c.9 2 2.6 3.7 4.6 4.6l1.6-1.3 2.9 2.3-1.4 2.3C7.5 14.9 1.1 8.5 1.3 2.6z"/></svg>
        0438 615 247
      </li>
      <li>
        <svg viewBox="0 0 16 16" aria-hidden="true"><rect x="1" y="3" width="14" height="10" rx="1" fill="var(--orange)"/><path d="M1.5 3.8L8 9l6.5-5.2" fill="none" stroke="#fff" stroke-width="1.3"/></svg>
        info@trivexplumbing.example.au
      </li>
      <li>
        <svg viewBox="0 0 16 16" aria-hidden="true"><circle cx="8" cy="8" r="7" fill="var(--orange)"/><path d="M1 8h14M8 1c-3 3-3 11 0 14M8 1c3 3 3 11 0 14" fill="none" stroke="#fff" stroke-width="1"/></svg>
        www.trivexplumbing.example.au
      </li>
    </ul>
  </section>

</main>
</body>
</html>
```